Quill & Harbor HVAC/R needs a Brantley Vireo high roof vehicle wrap design

Brand new Heating and Cooling/Refrigeration company in a town of around 44,000 people. Not a huge city but still need to make the van stand out as we are looking to eventually scale the business and branch out so we want to start exceptional branding immediately. We already have a logo but need graphics/colour scheme for a fleet of vehicles starting with Brantley Vireo Van K480 high roof. A local wrap installer made a PDF for us but it's extremely basic for graphics.

Target Market(s)

Homeowners and businesses

Industry/Entity Type

Refrigeration, heating and air conditioning

Colors
0054AA
0677BA
7BADD7
CADEEF
E8F1F8
0094D4
00A9DD
6FCCEA
C7EBF8
E9F6FB
00AB8E
00BBA5
67D7C9
C6EFE9
E9F9F6
EB3D1F
EC4F4E
F09395
F8D3D4
FCEDEE
A7469A
B969AE
D3A5CF
EDDBEB
F8F0F9

Requirements
Must have
• Snowflake graphics somewhere on the wrap, they can be faded into the background is ok
Nice to have
• darker background, Snowflakes, icecrystals/cubes, frost, flames, embers

```html
<!DOCTYPE html>
<html lang="en">
<head>
<meta charset="utf-8">
<title>Quill &amp; Harbor HVAC/R – Brantley Vireo Van K480 Wrap</title>
<link rel="stylesheet" href="https://fonts.googleapis.com/css2?family=Montserrat:wght@500;700&display=swap">
<style>
  :root {
    --page: #ececec;
    --wrap-black: #0b0b0d;
    --ink: #ffffff;
    --ice-deep: #0054aa;
    --ice-mid: #0094d4;
    --ice-light: #6fccea;
    --ice-pale: #c7ebf8;
    --ember-red: #eb3d1f;
    --ember-orange: #f47a1f;
    --ember-gold: #f6b73c;
    --accent-red: #ec4f4e;
  }
  * { box-sizing: border-box; margin: 0; padding: 0; }
  html, body { width: 1200px; height: 2700px; overflow: hidden; }
  body {
    background: var(--page);
    font-family: "Montserrat", Arial, sans-serif;
    color: var(--ink);
    position: relative;
  }
  .view {
    position: absolute;
    left: 60px;
    width: 1080px;
    height: 600px;
    background: var(--wrap-black);
    border-radius: 18px;
    overflow: hidden;
  }
  .view--front { top: 45px; }
  .view--driver { top: 705px; }
  .view--rear { top: 1365px; }
  .view--passenger { top: 2025px; }

  .brand { position: absolute; display: flex; align-items: center; gap: 12px; }
  .brand__dot {
    width: 16px; height: 16px; border-radius: 50%;
    background: var(--ice-light); flex: none;
  }
  .brand__name {
    font-weight: 700; font-size: 30px; letter-spacing: .5px; color: var(--ink);
    white-space: nowrap;
  }
  .tagline {
    position: absolute; font-size: 12px; font-weight: 500;
    letter-spacing: 2px; color: #cfd6dc; text-align: center; line-height: 1.7;
    white-space: nowrap;
  }

  .services {
    position: absolute;
    display: grid; grid-template-columns: auto auto;
    column-gap: 26px; row-gap: 12px;
    font-weight: 700; font-size: 20px;
    white-space: nowrap;
  }
  .service { display: flex; align-items: center; gap: 9px; }
  .service svg { width: 20px; height: 20px; flex: none; }
  .phone {
    position: absolute; display: flex; align-items: center; gap: 10px;
    font-weight: 700; font-size: 30px; letter-spacing: .5px;
    white-space: nowrap;
  }
  .phone svg { width: 26px; height: 26px; flex: none; }

  .fire-ice {
    position: absolute;
    background:
      linear-gradient(to top, var(--ice-pale) 0%, var(--ice-light) 22%, var(--ice-mid) 40%, rgba(0,84,170,0) 58%),
      linear-gradient(to right, var(--ember-red), var(--ember-orange) 35%, var(--ember-gold) 55%, var(--ember-orange) 75%, var(--ember-red));
  }
  .view--driver .fire-ice, .view--passenger .fire-ice {
    left: 0; right: 0; bottom: 0; height: 260px;
    -webkit-mask: linear-gradient(to bottom, transparent, #000 35%);
            mask: linear-gradient(to bottom, transparent, #000 35%);
  }
  .view--rear .fire-ice { left: 0; right: 0; top: 0; bottom: 0; opacity: .92; }

  .snowflake { position: absolute; opacity: .55; }
  .snowflake--faint { opacity: .22; }

  .frost {
    position: absolute; border-radius: 50%;
    background: radial-gradient(circle, rgba(199,235,248,.18), rgba(199,235,248,0) 70%);
  }
  .door-split {
    position: absolute; left: 539px; top: 0; bottom: 0; width: 2px; background: rgba(0,0,0,.6);
  }
  .rear-shade {
    position: absolute; left: 0; right: 0; top: 0; height: 120px;
    background: linear-gradient(to bottom, rgba(11,11,13,.95), rgba(11,11,13,0));
  }
  .rear-base {
    position: absolute; left: 0; right: 0; bottom: 0; height: 100px;
    background: linear-gradient(to top, rgba(11,11,13,.95), rgba(11,11,13,0));
  }
</style>
</head>
<body>

<svg width="0" height="0" style="position:absolute">
  <defs>
    <symbol id="tick" viewBox="0 0 24 24">
      <circle cx="12" cy="12" r="11" fill="#ffffff"/>
      <path d="M6.5 12.5l3.5 3.5 7.5-8" fill="none" stroke="#0b0b0d" stroke-width="2.6" stroke-linecap="round" stroke-linejoin="round"/>
    </symbol>
    <symbol id="phone" viewBox="0 0 24 24">
      <path fill="#ec4f4e" d="M6.6 10.8a15.1 15.1 0 0 0 6.6 6.6l2.2-2.2a1 1 0 0 1 1-.25 11.4 11.4 0 0 0 3.6.57 1 1 0 0 1 1 1V20a1 1 0 0 1-1 1A17 17 0 0 1 3 4a1 1 0 0 1 1-1h3.5a1 1 0 0 1 1 1c0 1.25.2 2.45.57 3.57a1 1 0 0 1-.25 1z"/>
    </symbol>
    <symbol id="flake" viewBox="-12 -12 24 24">
      <g stroke="#e9f6fb" stroke-width="1.6" stroke-linecap="round" fill="none">
        <path d="M0-11V11M-9.5-5.5L9.5 5.5M-9.5 5.5L9.5-5.5"/>
        <path d="M-3-8.5L0-5.5 3-8.5M-3 8.5L0 5.5 3 8.5"/>
      </g>
    </symbol>
  </defs>
</svg>

<!-- Front hood -->
<section class="view view--front" aria-label="Front view">
  <div class="frost" style="left:120px;top:60px;width:300px;height:300px"></div>
  <div class="frost" style="right:120px;top:160px;width:260px;height:260px"></div>
  <svg class="snowflake snowflake--faint" style="left:220px;top:140px" width="60" height="60"><use href="#flake"/></svg>
  <svg class="snowflake snowflake--faint" style="left:820px;top:260px" width="44" height="44"><use href="#flake"/></svg>
  <div class="brand" style="left:50%;top:272px;transform:translateX(-50%)">
    <span class="brand__dot"></span>
    <span class="brand__name">Quill &amp; Harbor HVAC/R</span>
  </div>
</section>

<!-- Driver side -->
<section class="view view--driver" aria-label="Driver side view">
  <div class="fire-ice" role="img" aria-label="Flames meeting ice crystals along the lower body"></div>
  <svg class="snowflake" style="left:80px;top:520px" width="40" height="40"><use href="#flake"/></svg>
  <svg class="snowflake" style="left:320px;top:540px" width="28" height="28"><use href="#flake"/></svg>
  <svg class="snowflake" style="left:610px;top:515px" width="44" height="44"><use href="#flake"/></svg>
  <svg class="snowflake" style="left:900px;top:535px" width="32" height="32"><use href="#flake"/></svg>
  <div class="frost" style="left:340px;top:40px;width:260px;height:260px"></div>
  <svg class="snowflake snowflake--faint" style="left:440px;top:70px" width="50" height="50"><use href="#flake"/></svg>
  <div class="brand" style="left:220px;top:150px">
    <span class="brand__dot"></span>
    <span class="brand__name">Quill &amp; Harbor HVAC/R</span>
  </div>
  <div class="tagline" style="left:220px;top:300px;width:400px">HEATING · COOLING · VENTILATION<br>RESIDENTIAL · COMMERCIAL</div>
  <div class="services" style="left:670px;top:110px">
    <div class="service"><svg><use href="#tick"/></svg>HVAC</div>
    <div class="service"><svg><use href="#tick"/></svg>Gas</div>
    <div class="service"><svg><use href="#tick"/></svg>Refrigeration</div>
    <div class="service"><svg><use href="#tick"/></svg>Electrical</div>
  </div>
  <div class="phone" style="left:670px;top:200px"><svg><use href="#phone"/></svg>555-014-2290</div>
</section>

<!-- Rear doors -->
<section class="view view--rear" aria-label="Rear view">
  <div class="fire-ice" role="img" aria-label="Full flames over a base of ice crystals"></div>
  <div class="rear-shade"></div>
  <div class="rear-base"></div>
  <svg class="snowflake" style="left:90px;top:400px" width="44" height="44"><use href="#flake"/></svg>
  <svg class="snowflake" style="left:330px;top:430px" width="30" height="30"><use href="#flake"/></svg>
  <svg class="snowflake" style="left:700px;top:410px" width="40" height="40"><use href="#flake"/></svg>
  <svg class="snowflake" style="left:950px;top:440px" width="30" height="30"><use href="#flake"/></svg>
  <div class="door-split"></div>
  <div class="services" style="left:50%;top:40px;transform:translateX(-50%)">
    <div class="service"><svg><use href="#tick"/></svg>HVAC</div>
    <div class="service"><svg><use href="#tick"/></svg>Gas</div>
    <div class="service"><svg><use href="#tick"/></svg>Refrigeration</div>
    <div class="service"><svg><use href="#tick"/></svg>Electrical</div>
  </div>
  <div class="brand" style="left:50%;top:262px;transform:translateX(-50%)">
    <span class="brand__dot"></span>
    <span class="brand__name">Quill &amp; Harbor HVAC/R</span>
  </div>
  <div class="phone" style="left:50%;bottom:40px;transform:translateX(-50%)"><svg><use href="#phone"/></svg>555-014-2290</div>
</section>

<!-- Passenger side -->
<section class="view view--passenger" aria-label="Passenger side view">
  <div class="fire-ice" role="img" aria-label="Ice crystals meeting flames and embers along the lower body"></div>
  <svg class="snowflake" style="left:110px;top:530px" width="34" height="34"><use href="#flake"/></svg>
  <svg class="snowflake" style="left:400px;top:515px" width="44" height="44"><use href="#flake"/></svg>
  <svg class="snowflake" style="left:700px;top:540px" width="28" height="28"><use href="#flake"/></svg>
  <svg class="snowflake" style="left:960px;top:520px" width="40" height="40"><use href="#flake"/></svg>
  <div class="frost" style="left:600px;top:40px;width:260px;height:260px"></div>
  <svg class="snowflake snowflake--faint" style="left:700px;top:70px" width="50" height="50"><use href="#flake"/></svg>
  <div class="services" style="left:70px;top:110px">
    <div class="service"><svg><use href="#tick"/></svg>HVAC</div>
    <div class="service"><svg><use href="#tick"/></svg>Gas</div>
    <div class="service"><svg><use href="#tick"/></svg>Refrigeration</div>
    <div class="service"><svg><use href="#tick"/></svg>Electrical</div>
  </div>
  <div class="phone" style="left:70px;top:200px"><svg><use href="#phone"/></svg>555-014-2290</div>
  <div class="brand" style="left:540px;top:150px">
    <span class="brand__dot"></span>
    <span class="brand__name">Quill &amp; Harbor HVAC/R</span>
  </div>
  <div class="tagline" style="left:540px;top:300px;width:400px">HEATING · COOLING · VENTILATION<br>RESIDENTIAL · COMMERCIAL</div>
</section>

</body>
</html>
```